Chorefinch/Jobwillow Style Site Design

I need a website similar to jobwillow or chorefinch, the marketing target is for Australian people. Please play with these 2 sites first if you are serious about the project.
I don't have very specific requirement, the functionalities should be like the reference site, but with different & unique design. What I want is a clean, elegant user interface with web2.0 modern style, especially homepage (When I implement your design into actual website, there will be much jquery & ajax modern technique used.)
I need design for the following pages:
1. homepage
2. login page
3. Sign up page
4. browse task page
5. post a task & confirmation page
6. Payment page
7. User Dashboard page
8. Single task page
The features must have photos of friendly looking helpers.
You can also check http://www.beta.errandmoth.example/ for reference. Be as creative & freshness as much as you can!
Target Market(s)
Australian people aging from 15 - 70.
Industry/Entity Type
Marketing
Look and feel
Each slider illustrates characteristics of the customer's brand and the style your logo design should communicate.

```html
<!DOCTYPE html>
<html lang="en">
<head>
<meta charset="utf-8">
<title>Nestwork – Payment Details</title>
<link href="https://fonts.googleapis.com/css2?family=PT+Sans:ital,wght@0,400;0,700;1,700&family=PT+Sans+Narrow:wght@400;700&display=swap" rel="stylesheet">
<style>
:root{
  --teal:#2a8cb3;
  --teal-dark:#1c6e91;
  --ink:#3a3a3a;
  --orange:#e48b0c;
  --page-bg:#ededed;
  --card-bg:#ffffff;
  --field-border:#d4d4d4;
  --footer-bg:#383838;
  --footer-text:#d8d8d8;
  --footer-icon:#5a5a5a;
}
*{margin:0;padding:0;box-sizing:border-box}
html,body{width:1200px;height:782px;overflow:hidden;background:var(--page-bg)}
body{font-family:"PT Sans",sans-serif;color:var(--ink)}
.page{position:relative;width:1400px;height:912px;transform:scale(.857143);transform-origin:0 0;background:var(--page-bg)}
.abs{position:absolute;white-space:nowrap}

/* header */
.topline{left:0;top:0;width:1400px;height:3px;background:var(--teal)}
.topband{left:0;top:3px;width:1400px;height:6px;background:#eef6f9}
.header{left:0;top:9px;width:1400px;height:100px;background:#fff;border-bottom:1px solid #dcdcdc}
.account-btn{top:3px;height:24px;width:70px;border-radius:0 0 4px 4px;background:linear-gradient(#3aa3c6,var(--teal-dark));color:#fff;font:700 11px/24px "PT Sans Narrow",sans-serif;text-align:center;letter-spacing:.3px}
.brand{left:222px;top:48px;font:700 38px/1 "PT Sans",sans-serif;color:var(--teal)}
.newsletter-btn{left:446px;top:46px;width:203px;height:46px;border-radius:4px;background:linear-gradient(#3ca6ca,var(--teal-dark));color:#fff;font:400 21px/44px "PT Sans Narrow",sans-serif;text-align:center;border:1px solid #17617f}
.nav-item{top:64px;font:400 13px/1 "PT Sans Narrow",sans-serif;color:#555;letter-spacing:.2px}
.nav-sep{top:57px;width:1px;height:28px;background:#d8d8d8}

/* content card */
.card{left:210px;top:129px;width:980px;height:646px;background:var(--card-bg)}
.section-title{font:400 23px/1 "PT Sans Narrow",sans-serif;color:var(--teal);letter-spacing:.2px}
.copy{font-size:11px;line-height:1;color:#444;letter-spacing:-.15px}
.link{color:var(--teal-dark)}
.field-label{width:260px;text-align:right;font:400 13px/1 "PT Sans Narrow",sans-serif;color:var(--teal);letter-spacing:.3px}
.field{height:31px;border:1px solid var(--field-border);border-radius:3px;background:linear-gradient(#fafafa,#f1f1f1)}
.select{font-size:11px;color:#777;padding:9px 10px}
.select-arrow{position:absolute;right:6px;top:6px;width:17px;height:17px;border:1px solid #888;border-radius:2px;background:linear-gradient(#fff,#ddd)}
.select-arrow svg{display:block;margin:4px auto 0}
.hint{font-size:11px;color:var(--orange)}
.divider{left:254px;top:532px;width:901px;height:1px;background:#d9d9d9}
.save-btn{height:32px;width:93px;border-radius:3px;background:linear-gradient(#3aa3c6,var(--teal-dark));border:1px solid #17617f;color:#fff;font:700 13px/30px "PT Sans Narrow",sans-serif;text-align:center}
.remove{font-size:11px;color:var(--orange)}
.pay-brand{left:344px;top:677px;font:700 19px/1 "PT Sans",sans-serif;color:var(--teal-dark)}

/* footer */
.footer{left:0;top:799px;width:1400px;height:113px;background:var(--footer-bg)}
.foot-link{font:400 10px/1 "PT Sans Narrow",sans-serif;color:var(--footer-text);letter-spacing:.2px}
.refer{left:724px;top:819px;width:246px;height:68px;background:#fff;border-radius:2px}
.refer-art{left:16px;top:8px;width:62px;height:54px;border-radius:27px;background:linear-gradient(135deg,#cfe7f1,#ffb233 45%,#f08a10)}
.refer-title{left:90px;top:7px;font:700 18px/1 "PT Sans",sans-serif;color:var(--teal);letter-spacing:.5px}
.refer-sub{left:92px;top:31px;font-size:9px;color:#444}
.refer-cta{left:92px;top:48px;font:700 9px/1 "PT Sans",sans-serif;color:var(--orange)}
.social{top:837px;width:31px;height:31px;border-radius:50%;background:var(--footer-icon)}
</style>
</head>
<body>
<div class="page">
  <div class="abs topline"></div>
  <div class="abs topband"></div>
  <header class="abs header"></header>
  <div class="abs account-btn" style="left:1046px">LOGIN</div>
  <div class="abs account-btn" style="left:1120px">SIGNUP</div>
  <div class="abs brand">Nestwork</div>
  <div class="abs newsletter-btn">SIGNUP NEWSLETTER</div>
  <nav>
    <span class="abs nav-item" style="left:677px">BROWSE TASKS</span>
    <span class="abs nav-sep" style="left:783px"></span>
    <span class="abs nav-item" style="left:819px">BECOME A RUNNER</span>
    <span class="abs nav-sep" style="left:951px"></span>
    <span class="abs nav-item" style="left:983px">POST A TASK</span>
    <span class="abs nav-sep" style="left:1081px"></span>
    <span class="abs nav-item" style="left:1112px">HOW IT WORKS</span>
  </nav>

  <main class="abs card"></main>
  <h1 class="abs section-title" style="left:248px;top:153px">PAYMENT DETAILS</h1>
  <p class="abs copy" style="left:248px;top:192px">Paying Nestwork for tasks I've been assigned. If you are assigned as the Runner of a task, you will be charged by Jobwillow a fee. When paying Nestwork, add or update your payment details below:</p>
  <h2 class="abs section-title" style="left:248px;top:233px">CARD DETAILS</h2>
  <p class="abs copy" style="left:248px;top:270px">Enter your credit card details to store against your profile. We currently accept Veloca and Mintcard cards.</p>

  <label class="abs field-label" style="left:251px;top:318px">CARD NUMBER</label>
  <div class="abs field" style="left:523px;top:307px;width:335px"></div>
  <label class="abs field-label" style="left:251px;top:366px">FULL NAME ON CARD</label>
  <div class="abs field" style="left:523px;top:355px;width:335px"></div>
  <label class="abs field-label" style="left:251px;top:416px">EXPIRY</label>
  <div class="abs field select" style="left:523px;top:405px;width:160px">Select month<span class="select-arrow"><svg width="9" height="6" viewBox="0 0 9 6"><path d="M1 1l3.5 4L8 1" fill="none" stroke="#333" stroke-width="1.6"/></svg></span></div>
  <div class="abs field select" style="left:698px;top:405px;width:160px">Select year<span class="select-arrow"><svg width="9" height="6" viewBox="0 0 9 6"><path d="M1 1l3.5 4L8 1" fill="none" stroke="#333" stroke-width="1.6"/></svg></span></div>
  <label class="abs field-label" style="left:251px;top:465px">CVC NUMBER</label>
  <div class="abs field" style="left:523px;top:454px;width:335px"></div>
  <p class="abs hint" style="left:526px;top:496px">You can find this on the rear of the card</p>

  <div class="abs divider"></div>
  <div class="abs save-btn" style="left:256px;top:555px">SAVE</div>

  <p class="abs copy" style="left:254px;top:605px">Paying Runners for tasks I've posted. When you post a task, you can select to pay the chosen runner by either Cash On Delivery or via PayWren. For PayWren, your saved details are shown below</p>
  <p class="abs copy link" style="left:254px;top:623px">Read more about how you can pay Runners for completing tasks.</p>

  <div class="abs pay-brand">PayWren</div>
  <label class="abs field-label" style="left:251px;top:681px">PAYWREN EMAIL</label>
  <div class="abs field" style="left:523px;top:670px;width:335px"></div>
  <div class="abs save-btn" style="left:523px;top:715px">SAVE</div>
  <span class="abs remove" style="left:625px;top:733px">Remove</span>

  <footer class="abs footer"></footer>
  <span class="abs foot-link" style="left:213px;top:835px">BROWSE TASKS</span>
  <span class="abs foot-link" style="left:304px;top:835px">|</span>
  <span class="abs foot-link" style="left:333px;top:835px">BECOME A RUNNER</span>
  <span class="abs foot-link" style="left:442px;top:835px">|</span>
  <span class="abs foot-link" style="left:472px;top:835px">POST A TASK</span>
  <span class="abs foot-link" style="left:553px;top:835px">|</span>
  <span class="abs foot-link" style="left:583px;top:835px">HOW IT WORKS</span>
  <span class="abs foot-link" style="left:214px;top:860px">©&nbsp;&nbsp; 2013&nbsp;&nbsp; NESTWORK&nbsp;&nbsp;|&nbsp;&nbsp; PRIVACY POLICY&nbsp;&nbsp;&nbsp; |&nbsp;&nbsp; TERMS &amp; CONDITIONS</span>

  <div class="abs refer">
    <div class="abs refer-art" role="img" aria-label="Friendly cartoon character with a speech bubble"></div>
    <div class="abs refer-title">TELL A FRIEND</div>
    <div class="abs refer-sub">AND GET $10 OFF!</div>
    <div class="abs refer-cta">INVITE FRIENDS NOW &raquo;</div>
  </div>

  <span class="abs social" style="left:1048px" aria-label="Social link"></span>
  <span class="abs social" style="left:1083px" aria-label="Social link"></span>
  <span class="abs social" style="left:1119px" aria-label="Social link"></span>
  <span class="abs social" style="left:1155px" aria-label="Feed link"></span>
</div>
</body>
</html>
```